AUDITING SERVICES FOR IMPORT/EXPORT/LOGISTICS

* PROCUREMENT OF PARTS / SERVICES
* BOAT POSITIONING

Industry/Entity Type

Auditing

Contact Information for Business Card

TRV CONSULTANTS
(TIDEWIND HULLCRAFT PTY LTD) 17 KESTREL VISTA CORALWOOD SHORES
DAVID HARTLEY 0417286342 JULIE-KATE HARTLEY 0417286918 (ON OPPOSITE SIDE)

```html
<!DOCTYPE html>
<html lang="en">
<head>
<meta charset="utf-8">
<title>TRV Consultants – Business Card</title>
<link rel="stylesheet" href="https://fonts.googleapis.com/css2?family=Tinos&family=Open+Sans:wght@700&display=swap">
<style>
  :root {
    --sky-top: #22a9e3;
    --sky-bottom: #137db5;
    --deep-top: #0869a3;
    --deep-bottom: #023a6b;
    --band-top: #2e2e2e;
    --band-mid: #000000;
    --text-light: #ffffff;
    --text-soft: #eef4fa;
  }
  html, body {
    margin: 0;
    padding: 0;
    width: 1200px;
    height: 741px;
    overflow: hidden;
  }
  .card {
    position: relative;
    width: 1200px;
    height: 741px;
    background: var(--deep-bottom);
  }
  .card__upper {
    position: absolute;
    left: 0; top: 0;
    width: 100%; height: 233px;
    background: linear-gradient(to bottom, var(--sky-top), var(--sky-bottom));
  }
  .card__band {
    position: absolute;
    left: 0; top: 233px;
    width: 100%; height: 185px;
    background: linear-gradient(to bottom, var(--band-top) 0%, #111 25%, var(--band-mid) 45%, var(--band-mid) 100%);
    display: flex;
    flex-direction: column;
    align-items: center;
    justify-content: center;
  }
  .card__lower {
    position: absolute;
    left: 0; top: 418px;
    width: 100%; height: 323px;
    background: linear-gradient(to bottom, var(--deep-top), var(--deep-bottom));
  }
  .company-name,
  .company-entity {
    margin: 0;
    font-family: "Tinos", "Times New Roman", serif;
    font-weight: 400;
    color: var(--text-light);
    font-size: 53px;
    line-height: 62px;
    letter-spacing: 0.5px;
    text-align: center;
  }
  .services {
    position: absolute;
    left: 0; top: 505px;
    width: 100%;
    margin: 0;
    padding: 0;
    list-style: none;
    text-align: center;
    font-family: "Open Sans", Arial, sans-serif;
    font-weight: 700;
    font-size: 32px;
    line-height: 43px;
    letter-spacing: 1px;
    color: var(--text-soft);
  }
</style>
</head>
<body>
  <div class="card">
    <div class="card__upper"></div>
    <header class="card__band">
      <h1 class="company-name">TRV CONSULTANTS</h1>
      <p class="company-entity">(TIDEWIND HULLCRAFT PTY LTD)</p>
    </header>
    <div class="card__lower"></div>
    <ul class="services">
      <li>- PROCUREMENT OF PARTS / SERVICES</li>
      <li>- BOAT POSITIONING</li>
    </ul>
  </div>
</body>
</html>
```